Either a trifold or double sided flyer/brochure

A flyer to help spark interest in a historic preservation project in Ashbury, NH--looking for something that captures the early 19th century rural village and mill times--American Primitive, Shaker, Cross Stitch Sampler...must be able to highlight home history as well as have all owners of house on a single page. Word document attached--can also provide files for the house painting, color photos, dorne photo, advertising photo or part of original settler map.
I like this brochure
http://tessavolkind.com/wordpress/quarnby-lodge-museum-brochure/
community stakeholders, residents,
Historic Preservation, House Museums.

```html
<!DOCTYPE html>
<html lang="en">
<head>
<meta charset="utf-8">
<title>The Hartwell Homestead History c. 1826</title>
<link href="https://fonts.googleapis.com/css2?family=PT+Sans&family=Tinos:wght@400;700&display=swap" rel="stylesheet">
<style>
:root{
  --canvas:#fdf5e8;
  --parchment:#eadcc0;
  --parchment-light:#f2e7d1;
  --rust:#8a3a12;
  --title:#8b2e12;
  --ink:#3b2a1f;
  --cream:#f4dfb4;
}
*{margin:0;padding:0;box-sizing:border-box}
html,body{width:753px;height:1200px;overflow:hidden;background:var(--canvas)}
.canvas{position:relative;width:753px;height:1200px}
.page{position:absolute;left:150px;width:453px;height:585px;overflow:hidden;box-shadow:0 3px 10px rgba(0,0,0,.25)}
.history{top:10px;background:var(--rust)}
.owners{top:605px;background:linear-gradient(180deg,var(--parchment-light),var(--parchment))}
.page svg.edge{position:absolute;inset:0}
.history-title{position:absolute;top:14px;left:10px;width:400px;text-align:center;font:700 20px Tinos,serif;color:var(--title);letter-spacing:.2px}
.history-sub{position:absolute;top:44px;left:10px;width:400px;text-align:center;font:400 13px Tinos,serif;color:var(--ink)}
.history-body{position:absolute;top:74px;left:30px;width:378px;text-align:center;font:400 8px/13.6px "PT Sans",sans-serif;color:var(--ink)}
.history-body p+p{margin-top:10px}
.invite{position:absolute;top:561px;left:0;width:430px;text-align:center;font:700 11px Tinos,serif;color:var(--title)}
.invite .dot{display:inline-block;width:9px;height:9px;border-radius:50%;background:var(--title);vertical-align:-1px;margin-right:5px}
.owners-title{position:absolute;top:12px;left:0;width:100%;text-align:center;font:700 15px Tinos,serif;color:var(--cream)}
.owners-sub{position:absolute;top:32px;left:0;width:100%;text-align:center;font:400 14px Tinos,serif;color:var(--cream)}
.painting-frame{position:absolute;left:64px;top:58px;width:324px;height:190px;background:#fff;padding:6px 6px 22px;box-shadow:0 2px 5px rgba(0,0,0,.35)}
.painting{width:100%;height:100%;background:linear-gradient(180deg,#9fb0bd 0%,#6f85a0 35%,#2f4d7a 55%,#3f5a2e 80%,#2d3f22 100%)}
.painting-caption{position:absolute;left:0;bottom:4px;width:100%;text-align:center;font:700 10px Tinos,serif;color:var(--title)}
.owner-list{position:absolute;left:20px;top:271px;width:282px;list-style:none;font:400 7.2px/9px Tinos,serif;color:var(--title)}
.owner-list li{position:relative;display:flex;padding-left:14px;margin-bottom:8px}
.owner-list li svg{position:absolute;left:0;top:1px}
.owner-list .who{width:220px}
.owner-list .when{width:60px}
.ad{position:absolute;left:318px;top:267px;width:92px;height:46px;background:linear-gradient(180deg,#e6dac2,#d8c9ac)}
.map{position:absolute;left:313px;top:317px;width:117px;height:115px;background:linear-gradient(135deg,#d7cdb9,#b9ad98);border:1px solid #9c8f78}
.house-photo{position:absolute;left:0;top:498px;width:453px;height:87px;background:linear-gradient(90deg,#5d4a1f,#b48a3a 35%,#d2a64e 55%,#7a5a22 80%,#3f3416)}
.portrait-frame{position:absolute;left:314px;top:443px;width:119px;height:124px;background:#fff;padding:6px 6px 12px;box-shadow:0 2px 5px rgba(0,0,0,.35)}
.portrait{width:100%;height:100%;background:linear-gradient(180deg,#8d8478,#5a5248 60%,#ddd8cf)}
</style>
</head>
<body>
<main class="canvas">

  <section class="page history">
    <svg class="edge" width="453" height="585" viewBox="0 0 453 585" aria-hidden="true">
      <polygon fill="#e9dbbd" points="0,0 415,0 419,8 413,18 420,30 416,44 424,60 420,78 428,96 424,118 431,140 427,166 434,190 430,214 437,240 433,268 440,296 436,322 441,350 436,380 441,408 437,436 442,462 437,490 441,516 436,540 440,560 432,572 420,568 400,575 380,569 350,576 0,576 0,520 8,512 4,496 12,482 6,470 0,466"/>
      <g stroke="#8b2e12" stroke-width="1.2" fill="none">
        <line x1="18" y1="64" x2="118" y2="64"/>
        <line x1="18" y1="64" x2="18" y2="568"/>
        <line x1="18" y1="568" x2="75" y2="568"/>
        <line x1="370" y1="568" x2="400" y2="568"/>
        <line x1="300" y1="64" x2="412" y2="64"/>
        <line x1="412" y1="64" x2="412" y2="560"/>
      </g>
      <g fill="#8b2e12">
        <circle cx="118" cy="64" r="2.5"/><circle cx="300" cy="64" r="2.5"/>
        <rect x="74" y="566" width="4" height="4"/><rect x="368" y="566" width="4" height="4"/>
      </g>
    </svg>
    <h1 class="history-title">The Hartwell Homestead History c. 1826</h1>
    <h2 class="history-sub">Ashbury, New Hampshire</h2>
    <div class="history-body">
      <p>In 1826, George S. Hartwell and his wife, Jane (Ashby) Hartwell purchased 26 acres from Robert Lane on the Quillan River, north of Thorne's Woolen Mill in South Ashbury, NH. This parcel was carved out lot #32 which was comprised of 268 acres that were deeded to John Lane (Robert Lane's grandfather) by Jeremiah Pratt and John Marsh on May 5, 1762. It is believed that Hartwell, who was blacksmith, built the house that currently stands at 27 Orchard Street in Ashbury, NH. He also built his forge on the site down by the river. It is likely that much of the forged hardware in the home was crafted by him. Feeling the need to leave Ashbury for a new frontier, Hartwell left town with his brother, Elwin, to purchase land in the emerging communities of Ambler County, NY. Before doing so, Hartwell sold the home, shop and buildings to Thomas Pell and his wife Alice (Grant) Pell in 1828.</p>
      <p>By trade, Thomas Pell was a cloth dresser and wool-carder. He was also a deeply religious man and served as deacon in the emerging, but still quite small, Baptist community. In those days, small groups of the Baptists and Methodists met in the Ridley Home for bible study, prayers and singing. The Ridleys were well known abolitionists and their house served as a stop on the Underground Railroad. Deacon Pell died in 1839 and his estate was managed by Samuel Grant—very likely a relative of Alice—who protected Alice's dower. The property was then sold to Elijah Brown Whitcomb and his wife Achsah (Rudd) Whitcomb</p>
      <p>Elijah was quite industrious and continued to expand the wool mill. He was an early investor in the Granite Hill Railroad and ceded a right of way to the railroad on the homestead. The mill eventually came under the control of his son, Henry A. Whitcomb, and operated until it burned down on April 20, 1874. Elijah passed away in 1877 and left the home to Mary Ellen Whitcomb who was most commonly known as "Ellen."</p>
      <p>Ellen Whitcomb was approached in 1891 by Allie Thorne, the owner of the Thorne's Mill Complex, to ask if she would be willing to rent out the home to a couple from Boston. This turned out to be Marian and Edward Lindell, the founders of the Lindell Colony, who ended up spending their first summer in Ashbury, NH in the home. Marian recalls in her writings: "You can't fail to remember the two-story farmhouse almost across from the road from the iron bridge, now occupied by the Dorne Family. It had never been painted and was a lovely soft gray in color. There were really only four rooms and a kitchen, spotlessly clean and adequately furnished, which really didn't mean much but some chairs, tables and beds. Then in the kitchen was something that fascinated me, a stone bowl into which the clearest of water was all the time pouring and then running off into a a drain...."</p>
      <p>The Dornes lived in this home for the longest time of any owner--and some refer to this area before the bridge, as Dornes Corner. This moment of stewardship began under Fred Parker Dorne and his wife Grace E. (Holt) Dorne around 1904 and lasted until 2015 when a descendant sold the home. The house is now under the stewardship of Edward M. Sousa and Albert A. Bristow, Jr. and will be undergoing a significant restoration.</p>
    </div>
    <p class="invite"><span class="dot"></span>They invite you to join their Hearthside Group</p>
  </section>

  <section class="page owners">
    <svg class="edge" width="453" height="585" viewBox="0 0 453 585" aria-hidden="true">
      <defs>
        <linearGradient id="band" x1="0" y1="0" x2="1" y2="1">
          <stop offset="0" stop-color="#5a2a12"/><stop offset=".5" stop-color="#6d3415"/><stop offset="1" stop-color="#3f1c0b"/>
        </linearGradient>
      </defs>
      <polygon fill="url(#band)" points="0,0 453,0 453,178 440,184 425,176 410,186 395,180 388,188 388,60 64,60 64,186 50,180 35,188 20,181 0,188"/>
    </svg>
    <h1 class="owners-title">Hartwell Homestead c. 1826,</h1>
    <h2 class="owners-sub">Dornes Corner, Ashbury, New Hampshire</h2>
    <figure class="painting-frame">
      <div class="painting" role="img" aria-label="Folk painting of the white farmhouse with blue roof and attached barn"></div>
      <figcaption class="painting-caption">Owners of 27 Orchard Street Ashbury, New Hampshire</figcaption>
    </figure>
    <ul class="owner-list">
      <li><svg width="9" height="9" viewBox="0 0 10 10"><circle cx="5" cy="5" r="3.8" fill="none" stroke="#8b2e12"/><path d="M5 3v2.2l1.5 1" stroke="#8b2e12" fill="none"/></svg><span class="who">Robert Lane (grandson of John Lane) owned the land</span><span class="when">18260</span></li>
      <li><svg width="9" height="9" viewBox="0 0 10 10"><circle cx="5" cy="5" r="3.8" fill="none" stroke="#8b2e12"/><path d="M5 3v2.2l1.5 1" stroke="#8b2e12" fill="none"/></svg><span class="who">George S. Hartwell and Jane (Ashby) Hartwell</span><span class="when">1826-1828</span></li>
      <li><svg width="9" height="9" viewBox="0 0 10 10"><circle cx="5" cy="5" r="3.8" fill="none" stroke="#8b2e12"/><path d="M5 3v2.2l1.5 1" stroke="#8b2e12" fill="none"/></svg><span class="who">Deacon Thomas Pell and Alice (Grant) Pell (Baptist)</span><span class="when">1828-1839</span></li>
      <li><svg width="9" height="9" viewBox="0 0 10 10"><circle cx="5" cy="5" r="3.8" fill="none" stroke="#8b2e12"/><path d="M5 3v2.2l1.5 1" stroke="#8b2e12" fill="none"/></svg><span class="who">Elijah Brown Whitcomb and Achsah (Rudd) Whitcomb<br>(mortgage between Samuel Grant and Whitcomb is 1845)</span><span class="when">1839-1877</span></li>
      <li><svg width="9" height="9" viewBox="0 0 10 10"><circle cx="5" cy="5" r="3.8" fill="none" stroke="#8b2e12"/><path d="M5 3v2.2l1.5 1" stroke="#8b2e12" fill="none"/></svg><span class="who">Mary Ellen Whitcomb</span><span class="when">1877-1898</span></li>
      <li><svg width="9" height="9" viewBox="0 0 10 10"><circle cx="5" cy="5" r="3.8" fill="none" stroke="#8b2e12"/><path d="M5 3v2.2l1.5 1" stroke="#8b2e12" fill="none"/></svg><span class="who">James Conley</span><span class="when">1898-1904</span></li>
      <li><svg width="9" height="9" viewBox="0 0 10 10"><circle cx="5" cy="5" r="3.8" fill="none" stroke="#8b2e12"/><path d="M5 3v2.2l1.5 1" stroke="#8b2e12" fill="none"/></svg><span class="who">Fred Parker Dorne and Grace E. (Holt) Dorne</span><span class="when">1904-1956</span></li>
      <li><svg width="9" height="9" viewBox="0 0 10 10"><circle cx="5" cy="5" r="3.8" fill="none" stroke="#8b2e12"/><path d="M5 3v2.2l1.5 1" stroke="#8b2e12" fill="none"/></svg><span class="who">Elinor (Dorne) Halvorsen and Frank O Halvorsen<br>(Elinor was born in house on July 29, 1911)</span><span class="when">1955-1998</span></li>
      <li><svg width="9" height="9" viewBox="0 0 10 10"><circle cx="5" cy="5" r="3.8" fill="none" stroke="#8b2e12"/><path d="M5 3v2.2l1.5 1" stroke="#8b2e12" fill="none"/></svg><span class="who">James H. Kettleman and Maria Ruiz Kettleman<br>(James was nephew of Elinor (Dorne) Halvorsen)</span><span class="when">1998-2015</span></li>
      <li><svg width="9" height="9" viewBox="0 0 10 10"><circle cx="5" cy="5" r="3.8" fill="none" stroke="#8b2e12"/><path d="M5 3v2.2l1.5 1" stroke="#8b2e12" fill="none"/></svg><span class="who">Millbrook Commons</span><span class="when">2015-2022</span></li>
      <li><svg width="9" height="9" viewBox="0 0 10 10"><circle cx="5" cy="5" r="3.8" fill="none" stroke="#8b2e12"/><path d="M5 3v2.2l1.5 1" stroke="#8b2e12" fill="none"/></svg><span class="who">Edward M. Sousa and Albert A. Bristow, Jr.</span><span class="when">2022</span></li>
    </ul>
    <div class="ad" role="img" aria-label="Antique newspaper advertisement for the wool carder and cloth dresser"></div>
    <div class="map" role="img" aria-label="Portion of the original settler lot map along the river"></div>
    <div class="house-photo" role="img" aria-label="Colour photograph of the yellow homestead among autumn trees"></div>
    <figure class="portrait-frame">
      <div class="portrait" role="img" aria-label="Vintage black and white photograph of a former owner couple seated indoors"></div>
    </figure>
  </section>

</main>
</body>
</html>
```